Menu Board 1000mmx500mm re-design

I would like to re-design exiting menu board 1000mmx500mm. Current board letters are bit to small to read. I would like to have pictures (attached) of the food offered on it and at the same time to create balance between pictures and size of the text to be easily readable. Fonts and colours are up to designer choice but prefer warm and bright colours rather anything dark.

Target Market(s)

Food industry

Industry/Entity Type

Food

Font styles to use
Other font styles liked:
• I leave font choice to designer

Colors
FFC000
F8CF3A
FAE287
FDF2CF
FEFAEE
F0912C
F2A743
F7CA91
FBE8D2
FDF5EE
EE7325
F08F49
F5BC92
FAE3D3
FDF4ED

Requirements
Must have
• Pictures + Text
Nice to have
• Balance between images and text.
Should not have
• Can't think of any

```html
<!DOCTYPE html>
<html lang="en">
<head>
<meta charset="utf-8">
<title>Menu Board</title>
<link rel="stylesheet" href="https://fonts.googleapis.com/css2?family=Montserrat:wght@500;700;800&display=swap">
<style>
  :root {
    --page-bg: #FDBA5C;
    --board-cream: #FCF2D3;
    --orange-deep: #EE7325;
    --orange-mid: #F0912C;
    --orange-soft: #F5BC92;
    --amber: #FFC000;
    --ink: #141414;
    --dot: #F8E2A6;
  }
  html, body {
    margin: 0;
    padding: 0;
    width: 1200px;
    height: 1200px;
    overflow: hidden;
    background: var(--page-bg);
  }
  .menu-board {
    position: absolute;
    left: 0;
    top: 300px;
    width: 1200px;
    height: 600px;
    display: block;
  }
  .board-bg { fill: var(--board-cream); }
  .photo-frame { fill: none; stroke: var(--orange-deep); stroke-width: 14; }
  .item-name {
    font-family: 'Montserrat', sans-serif;
    font-weight: 800;
    font-size: 35px;
    fill: var(--ink);
  }
  .item-price {
    font-family: 'Montserrat', sans-serif;
    font-weight: 800;
    font-size: 35px;
    fill: var(--orange-deep);
  }
  .item-desc {
    font-family: 'Montserrat', sans-serif;
    font-weight: 500;
    font-size: 18px;
    fill: var(--ink);
  }
  .sauces-title {
    font-family: 'Montserrat', sans-serif;
    font-weight: 800;
    font-size: 40px;
    fill: var(--orange-deep);
  }
  .sauces-list {
    font-family: 'Montserrat', sans-serif;
    font-weight: 700;
    font-size: 29px;
    fill: var(--ink);
  }
  .deco-dot { fill: var(--dot); }
</style>
</head>
<body>
<svg class="menu-board" viewBox="0 0 1812 906" xmlns="http://www.w3.org/2000/svg">
  <defs>
    <linearGradient id="wrapTone" x1="0" y1="0" x2="1" y2="1">
      <stop offset="0" stop-color="#E9D7C6"/>
      <stop offset="1" stop-color="#B9815A"/>
    </linearGradient>
    <linearGradient id="ciabattaTone" x1="0" y1="0" x2="0" y2="1">
      <stop offset="0" stop-color="#ECEBEA"/>
      <stop offset="1" stop-color="#C4844C"/>
    </linearGradient>
    <linearGradient id="potatoTone" x1="0" y1="0" x2="1" y2="1">
      <stop offset="0" stop-color="#D9902F"/>
      <stop offset="1" stop-color="#5A3A22"/>
    </linearGradient>
    <linearGradient id="chickenTone" x1="0" y1="0" x2="1" y2="0">
      <stop offset="0" stop-color="#EDEAE0"/>
      <stop offset="1" stop-color="#D49A4E"/>
    </linearGradient>
    <radialGradient id="beetTone" cx="0.5" cy="0.5" r="0.5">
      <stop offset="0" stop-color="#D8C9B8"/>
      <stop offset="1" stop-color="#8E3548"/>
    </radialGradient>
  </defs>

  <rect class="board-bg" x="0" y="0" width="1812" height="906"/>

  <g class="deco-dots">
    <circle class="deco-dot" cx="592" cy="155" r="14"/>
    <circle class="deco-dot" cx="384" cy="280" r="14"/>
    <circle class="deco-dot" cx="592" cy="287" r="12"/>
    <circle class="deco-dot" cx="1243" cy="195" r="12"/>
    <circle class="deco-dot" cx="1263" cy="287" r="8"/>
    <circle class="deco-dot" cx="34" cy="492" r="9"/>
    <circle class="deco-dot" cx="545" cy="743" r="8"/>
    <circle class="deco-dot" cx="1330" cy="730" r="6"/>
  </g>

  <!-- Corner photos -->
  <path class="photo photo-wrap" role="img" aria-label="Photo of a grilled chicken wrap on a wooden board"
        fill="url(#wrapTone)"
        d="M0 0 H540 C520 130 460 230 300 262 C160 288 60 310 0 372 Z"/>
  <path class="photo-frame" d="M540 0 C520 130 460 230 300 262 C160 288 60 310 0 372"/>

  <path class="photo photo-ciabatta" role="img" aria-label="Photo of a chicken and rocket ciabatta on a wooden board"
        fill="url(#ciabattaTone)"
        d="M1248 0 H1812 V368 C1760 320 1700 292 1500 272 C1340 256 1272 150 1248 0 Z"/>
  <path class="photo-frame" d="M1248 0 C1272 150 1340 256 1500 272 C1700 292 1760 320 1812 368"/>

  <path class="photo photo-potatoes" role="img" aria-label="Photo of roasted potatoes with thyme"
        fill="url(#potatoTone)"
        d="M0 690 C220 680 510 692 620 790 C660 840 690 880 720 906 H0 Z"/>
  <path class="photo-frame" d="M0 690 C220 680 510 692 620 790 C660 840 690 880 720 906"/>

  <path class="photo photo-chicken-box" role="img" aria-label="Photo of roast chicken with veggie rice"
        fill="url(#chickenTone)"
        d="M1812 688 C1600 684 1360 700 1255 790 C1210 840 1180 880 1150 906 H1812 Z"/>
  <path class="photo-frame" d="M1812 688 C1600 684 1360 700 1255 790 C1210 840 1180 880 1150 906"/>

  <!-- Heading lettering -->
  <rect class="menu-lettering" role="img" aria-label="Hand-lettered MENU heading with orange splashes"
        x="640" y="55" width="540" height="210" rx="40" fill="#F5BC92" opacity="0.55"/>

  <!-- Central feature photo -->
  <ellipse class="photo photo-beetroot-wrap" role="img" aria-label="Photo of a halved beetroot chicken wrap"
           cx="900" cy="490" rx="240" ry="190" fill="url(#beetTone)"/>

  <!-- Left column -->
  <g class="menu-column menu-left">
    <text class="item-name" x="83" y="370">CIABATTA.....................</text>
    <text class="item-price" x="580" y="370" text-anchor="end">£6</text>
    <text class="item-desc" x="88" y="394">Roti Chicken, Rucola, Caramelized Onions,</text>
    <text class="item-desc" x="88" y="416">Tomato, Fresh Onion</text>

    <text class="item-name" x="83" y="466">WRAP............................</text>
    <text class="item-price" x="580" y="466" text-anchor="end">£7</text>
    <text class="item-desc" x="83" y="490">Roti Chicken, Crunchy Slaw, Tomato, Fresh Onions,</text>
    <text class="item-desc" x="83" y="512">&amp; Sauce of your choice</text>

    <text class="item-name" x="83" y="567">BEETROOT WRAP.......</text>
    <text class="item-price" x="580" y="567" text-anchor="end">£8</text>
    <text class="item-desc" x="83" y="592">Roti Chicken, Crunchy Slaw, Tomato, Fresh Onions,</text>
    <text class="item-desc" x="83" y="614">&amp; Sauce of your choice</text>

    <text class="item-name" x="83" y="662">WATER.........................</text>
    <text class="item-price" x="580" y="662" text-anchor="end">£1</text>
  </g>

  <!-- Right column -->
  <g class="menu-column menu-right">
    <text class="item-name" x="1230" y="370">1/4 CHICKEN BOX.......</text>
    <text class="item-price" x="1748" y="370" text-anchor="end">£9</text>
    <text class="item-desc" x="1230" y="396">Roti Chicken,  Veggie Rice &amp; Salad</text>

    <text class="item-name" x="1230" y="466">1/2 CHICKEN BOX.......</text>
    <text class="item-price" x="1748" y="466" text-anchor="end">£14</text>
    <text class="item-desc" x="1230" y="492">Roti Chicken,  Veggie Rice &amp; Salad</text>

    <text class="item-name" x="1230" y="567">ROASTED POTATOES...</text>
    <text class="item-price" x="1756" y="567" text-anchor="end">£2.5</text>
    <text class="item-desc" x="1230" y="592">Thyme &amp; Garlic</text>

    <text class="item-name" x="1230" y="662">CAN &amp; JUICES..............</text>
    <text class="item-price" x="1752" y="662" text-anchor="end">£1.8</text>
  </g>

  <!-- Sauces -->
  <g class="sauces">
    <text class="sauces-title" x="906" y="757" text-anchor="middle">SAUCES</text>
    <text class="sauces-list" x="906" y="803" text-anchor="middle">SIGNATURE, BBQ, PIRI PIRI</text>
    <text class="sauces-list" x="906" y="848" text-anchor="middle">SWEET CHILLI &amp; GARLIC MAYO</text>
  </g>
</svg>
</body>
</html>
```